Simple Business Cards for Self-employed Coach

Simple business card with a design that includes the QLT logo.
Using either only the logo color or additional colors that match the logo.

Meridian Guides reach deeply into the past, gathering wisdom from East and West, while still staying current with the frontiers of new discovery in cognitive science, genetics, and other disciplines. see https://www.brightharborpath.example/what-is-integral-coaching/

Target Market(s)

Coaching Clients in Tokyo /Asia; in business organizations, but also outside

Industry/Entity Type

Life Coaching

Contact Information for Business Card

Lukas Brenning
Certified Meridian Guide

3-2-48 Kamiyoshi
Nakarino 164-0392
Tokyo, Japan

Phone: +81 70 4817 5062
E-Mail: lukas.brenning@mailora.example

Font styles to use
Sans Serif

Colors
00a990

Requirements
Must have
• include uploaded logo
• color fitting with QLT logo color
Nice to have
• simple, elegant design
Should not have
• clutter

```html
<!DOCTYPE html>
<html lang="en">
<head>
<meta charset="utf-8">
<title>Lukas Brenning – Business Card</title>
<link rel="stylesheet" href="https://fonts.googleapis.com/css2?family=Roboto:wght@300;400&display=swap">
<style>
  :root {
    --backdrop: #1c1a1b;
    --teal-light: #2bb39a;
    --teal-mid: #22a794;
    --teal-deep: #139a8c;
    --brand-teal: #127d74;
    --paper: #ffffff;
  }
  * { margin: 0; padding: 0; box-sizing: border-box; }
  html, body {
    width: 1200px;
    height: 1200px;
    overflow: hidden;
    background: var(--backdrop);
    font-family: "Roboto", Arial, sans-serif;
  }
  .business-card {
    position: absolute;
    left: 127px;
    top: 331px;
    width: 945px;
    height: 539px;
    overflow: hidden;
  }
  .card-background {
    position: absolute;
    inset: 0;
    background: linear-gradient(170deg, var(--teal-light) 0%, var(--teal-mid) 55%, var(--teal-deep) 100%);
  }
  .brand-plate {
    position: absolute;
    left: 0;
    top: 197px;
    width: 424px;
    height: 147px;
    background: var(--paper);
    display: flex;
    align-items: center;
    justify-content: center;
    gap: 22px;
  }
  .brand-square {
    width: 44px;
    height: 44px;
    background: var(--brand-teal);
  }
  .brand-name {
    font-weight: 400;
    font-size: 64px;
    letter-spacing: 10px;
    color: var(--brand-teal);
    line-height: 1;
  }
  .contact-block {
    position: absolute;
    left: 473px;
    top: 106px;
    color: var(--paper);
    font-weight: 300;
    font-size: 28px;
    line-height: 36px;
  }
  .person-name {
    font-weight: 400;
    font-size: 35px;
    line-height: 40px;
  }
  .person-title { margin-bottom: 40px; }
  .address { margin-bottom: 35px; }
  .label { font-weight: 400; }
</style>
</head>
<body>
  <div class="business-card">
    <div class="card-background" role="img" aria-label="Soft flowing teal background artwork"></div>

    <div class="brand-plate">
      <span class="brand-square"></span>
      <span class="brand-name">QLT</span>
    </div>

    <div class="contact-block">
      <p class="person-name">Lukas Brenning</p>
      <p class="person-title">Certified Meridian Guide</p>
      <p class="address">3-2-48 Kamiyoshi<br>Nakarino 164-0392<br>Tokyo, Japan</p>
      <p class="phone"><span class="label">P:</span> +81 70 4817 5062</p>
      <p class="email"><span class="label">E:</span> lukas.brenning@mailora.example</p>
    </div>
  </div>
</body>
</html>
```